QURNB Apothecary
-Designs for stationary is needed: cards, letterhead, envelopes etc...
- The tagline under the mortar and pestle should be placed in one straightline across (instead placed as 2 lines)
- using symbol for email, phone e.g.#75 is good. Note the symbol for email I believe is an envelope.
- use recycle symbol on back (not words) e.g.87
- Background color should be grey (on the back only)
- On the back include faded mortar and pestle with capsules, tagline and recycle symbols e.g. #83
- Don't list website along with phone, fax, email. Place it to the corner in the back and front

```html
<!DOCTYPE html>
<html lang="en">
<head>
<meta charset="utf-8">
<title>QURNB Apothecary Stationery</title>
<link href="https://fonts.googleapis.com/css2?family=Open+Sans:wght@400;700&display=swap" rel="stylesheet">
<style>
:root{
  --stage:#3a3b3d;
  --paper:#ffffff;
  --card-grey:#d9dadb;
  --brand-blue:#1f4f8f;
  --brand-green:#5c9a2e;
  --deep-green:#3f7a2a;
  --sky-blue:#2f7fd0;
  --ink:#555a60;
  --label:#b9bbbe;
  --faint:#e6ece4;
}
*{margin:0;padding:0;box-sizing:border-box}
html,body{width:1200px;height:346px;overflow:hidden}
body{background:var(--stage);font-family:"Open Sans",Arial,sans-serif;position:relative;color:var(--ink)}
.piece{position:absolute;background:var(--paper);box-shadow:0 2px 6px rgba(0,0,0,.45);overflow:hidden}
.brand{display:flex;align-items:center;gap:3px}
.brand-dot{width:8px;height:8px;border-radius:50%;background:var(--brand-green);flex:none}
.brand-name{color:var(--brand-blue);font-weight:700;white-space:nowrap}
.tagline{color:var(--brand-green);white-space:nowrap}
.small{font-size:4px;line-height:6px;color:var(--ink);white-space:nowrap}
.label{position:absolute;font-size:5px;color:var(--label);white-space:nowrap}
.watermark{position:absolute;border-radius:50%;background:radial-gradient(circle,var(--faint) 0%,rgba(230,236,228,0) 70%)}
.bands{position:absolute;left:0;right:0;bottom:0;height:5px;display:flex}
.bands .blue{flex:3;background:var(--brand-blue)}
.bands .green{flex:1;background:var(--brand-green)}

/* identity block */
.identity{position:absolute;left:14px;top:10px;width:140px}
.identity .brand-name{font-size:12px}
.identity .brand-dot{width:16px;height:16px}
.identity .tagline{font-size:4px;margin-top:3px}
.identity .concept{font-size:5px;color:var(--label);margin-top:6px}

/* business cards */
.card{left:12px;width:104px;height:56px;border-radius:3px}
.card-front{top:118px}
.card-front .brand{position:absolute;left:8px;top:7px}
.card-front .brand-dot{width:7px;height:7px}
.card-front .brand-name{font-size:6.5px}
.card-front .person{position:absolute;left:8px;top:26px;font-size:4px;font-weight:700;color:var(--brand-blue);white-space:nowrap}
.card-front .contact{position:absolute;left:8px;top:32px}
.card-back{top:204px;background:var(--card-grey)}
.card-back .watermark{left:28px;top:4px;width:48px;height:48px;background:radial-gradient(circle,#c7d2c2 0%,rgba(199,210,194,0) 70%)}
.card-back .recycle{position:absolute;right:6px;bottom:6px}
.card-back .web{position:absolute;left:6px;bottom:5px;font-size:4px;color:var(--brand-blue)}

/* letterheads */
.letterhead{top:10px;width:204px;height:297px}
.lh-1{left:173px}
.lh-2{left:403px}
.letterhead .brand{position:absolute;left:30px;top:12px}
.letterhead .brand-name{font-size:7.5px}
.letterhead .tagline{position:absolute;left:30px;top:23px;font-size:3px}
.letterhead .contact{position:absolute;left:128px;top:11px;font-size:3.5px;line-height:5px}
.letterhead .watermark{left:47px;top:90px;width:110px;height:110px}
.letterhead .footer{position:absolute;left:0;right:0;bottom:8px;text-align:center;font-size:3.5px}

/* envelopes */
.env{left:636px;width:216px;height:110px}
.env-1{top:56px}
.env-2{top:212px}
.env .brand{position:absolute;left:10px;top:10px}
.env .brand-name{font-size:8px}
.env .return{position:absolute;left:10px;top:22px}
.env .watermark{left:110px;top:20px;width:80px;height:80px}

.env-back{left:869px;width:307px;height:110px}
.eb-green{top:48px}
.eb-blue{top:135px}
.eb-white{top:220px}
.env-back svg{position:absolute;left:0;top:0}
.flap-mark{position:absolute;left:140px;top:10px;width:28px;height:22px;border-radius:50%}
</style>
</head>
<body>

<section class="identity">
  <div class="brand"><span class="brand-dot"></span><span class="brand-name">QURNB Apothecary</span></div>
  <p class="tagline">Natural Remedies Compounded With Care</p>
  <p class="concept">Stationery Concept</p>
</section>

<article class="piece card card-front">
  <div class="brand"><span class="brand-dot"></span><span class="brand-name">QURNB Apothecary</span></div>
  <p class="person">Dana Morell, Pharmacist</p>
  <div class="contact small">
    <p>&#9742; (555) 210-4471</p>
    <p>&#9993; hello@qurnb.com</p>
  </div>
</article>
<span class="label" style="left:12px;top:177px">Business Card Front</span>

<article class="piece card card-back">
  <div class="watermark" role="img" aria-label="Faded mortar and pestle with capsules"></div>
  <span class="web">www.qurnb.com</span>
  <svg class="recycle" width="10" height="10" viewBox="0 0 10 10" aria-label="Recycle symbol">
    <path d="M5 1 L8 6 H2 Z" fill="none" stroke="var(--deep-green)" stroke-width="1"/>
  </svg>
</article>
<span class="label" style="left:12px;top:263px">Business Card Back</span>

<article class="piece letterhead lh-1">
  <div class="brand"><span class="brand-dot"></span><span class="brand-name">QURNB Apothecary</span></div>
  <p class="tagline">Natural Remedies Compounded With Care</p>
  <div class="contact small">
    <p>&#9742; (555) 210-4471</p>
    <p>&#9993; hello@qurnb.com</p>
    <p>48 Linden Row, Harbor City</p>
  </div>
  <div class="watermark" role="img" aria-label="Faded mortar and pestle with prescription mark"></div>
  <p class="footer small">www.qurnb.com</p>
  <div class="bands"><span class="blue"></span><span class="green"></span></div>
</article>
<span class="label" style="left:173px;top:312px">Letterhead Page 1</span>

<article class="piece letterhead lh-2">
  <div class="brand"><span class="brand-dot"></span><span class="brand-name">QURNB Apothecary</span></div>
  <p class="tagline">Natural Remedies Compounded With Care</p>
  <div class="watermark" role="img" aria-label="Faded mortar and pestle with prescription mark"></div>
  <p class="footer small">www.qurnb.com</p>
  <div class="bands"><span class="blue"></span><span class="green"></span></div>
</article>
<span class="label" style="left:403px;top:312px">Letterhead Page 2</span>

<article class="piece env env-1">
  <div class="brand"><span class="brand-dot"></span><span class="brand-name">QURNB Apothecary</span></div>
  <p class="return small">48 Linden Row, Harbor City</p>
  <div class="watermark" role="img" aria-label="Faded mortar and pestle"></div>
  <div class="bands"><span class="blue"></span><span class="green"></span></div>
</article>
<span class="label" style="left:636px;top:170px">Envelope Front</span>

<article class="piece env env-2">
  <div class="brand"><span class="brand-dot"></span><span class="brand-name">QURNB Apothecary</span></div>
  <p class="return small">48 Linden Row, Harbor City</p>
  <div class="watermark" role="img" aria-label="Faded mortar and pestle"></div>
  <div class="bands"><span class="blue"></span><span class="green"></span></div>
</article>
<span class="label" style="left:636px;top:326px">Envelope Front</span>

<article class="piece env-back eb-green">
  <svg width="307" height="110" viewBox="0 0 307 110">
    <rect width="307" height="110" fill="#f4f5f4"/>
    <path d="M0 0 H307 L170 58 Q153 64 137 58 Z" fill="var(--deep-green)"/>
  </svg>
  <div class="flap-mark" role="img" aria-label="Mortar and pestle emblem" style="background:#8fbf6a"></div>
</article>

<article class="piece env-back eb-blue">
  <svg width="307" height="110" viewBox="0 0 307 110">
    <rect width="307" height="110" fill="#f4f5f4"/>
    <path d="M0 0 H307 L170 58 Q153 64 137 58 Z" fill="var(--sky-blue)"/>
  </svg>
  <div class="flap-mark" role="img" aria-label="Mortar and pestle emblem" style="background:#8bbbe8"></div>
</article>

<article class="piece env-back eb-white" style="height:104px">
  <svg width="307" height="104" viewBox="0 0 307 104">
    <rect width="307" height="104" fill="#f7f7f7"/>
    <path d="M0 0 L153 58 L307 0" fill="none" stroke="#cfd1d3" stroke-width="1"/>
    <path d="M0 104 L120 46 M307 104 L186 46" fill="none" stroke="#dcdedf" stroke-width="1"/>
  </svg>
</article>
<span class="label" style="left:1000px;top:330px">Envelope Back</span>

</body>
</html>
```